Travel agency website refresh

I want to refresh and simplify my current Wordpress.com website. Same general color scheme but modernize and make it user friendly for all devices. Must work with Wordpress. No live booking engines. We are a boutique luxury travel agency. Think luxury, vacation, boho chic, elegant, lush, tropical, cruises, first class. Romance and adventure.
Updates

I’ve guaranteed the project so I’m hoping to see more quality entries to make a decision

Target Market(s)

Luxury travelers

Industry/Entity Type

Travel

Coding

Coded - Design and coding required

Number of Pages Required

5+ page

Font styles to use
Sans Serif

Colors
0094D4
00A9DD
6FCCEA
C7EBF8
E9F6FB

Requirements
Must have
• Compatible with Wordpress.com, homepage, about page, contact page, faq page
Nice to have
• The homepage should quickly tell the consumer the type of travel I specialize in. My current website has this (journeywithmerel.example). I’d like to incorporate the about me as a preview on the home page.
Should not have
• Harsh colors, look generic

```html
<!DOCTYPE html>
<html lang="en">
<head>
<meta charset="utf-8">
<title>Travel by Merel — Creating Memorable Vacations</title>
<link rel="stylesheet" href="https://fonts.googleapis.com/css2?family=Oswald:wght@300;400&family=Poppins:ital,wght@0,400;1,400&display=swap">
<style>
:root{
  --blue-deep:#0094D4;
  --blue:#00A9DD;
  --blue-mid:#6FCCEA;
  --blue-soft:#C7EBF8;
  --blue-pale:#E9F6FB;
  --ink:#1d1d1f;
  --text:#444;
  --white:#fff;
}
*{margin:0;padding:0;box-sizing:border-box}
html,body{width:1200px;height:4481px;overflow:hidden;background:var(--white)}
body{position:relative;font-family:'Poppins',sans-serif;color:var(--text)}
.abs{position:absolute}
.heading{font-family:'Oswald',sans-serif;font-weight:300;color:var(--ink);text-transform:uppercase}
.btn{position:absolute;display:flex;align-items:center;justify-content:center;border:2px solid var(--blue-mid);color:var(--blue-mid);font-family:'Oswald',sans-serif;font-weight:300;font-size:23px;text-transform:uppercase;background:var(--white);width:184px;height:52px;text-decoration:none}
.photo{position:absolute;overflow:hidden}
.photo::after{content:"";position:absolute;inset:0;box-shadow:inset 0 0 120px rgba(0,0,0,.18)}

/* header */
.logo{position:absolute;left:75px;top:17px;width:200px;display:flex;flex-direction:column;align-items:center}
.logo .mark{width:92px;height:92px;border-radius:50%;background:var(--blue-soft)}
.logo .name{font-family:'Oswald',sans-serif;font-weight:400;font-size:30px;color:#666;letter-spacing:.5px;margin-top:6px;white-space:nowrap}
.nav{position:absolute;left:381px;top:31px;display:flex;gap:33px;font-family:'Oswald',sans-serif;font-weight:300;font-size:16px;text-transform:uppercase;color:var(--ink)}
.nav .current{color:var(--blue-mid)}

/* hero */
.hero-panel{left:793px;top:82px;width:407px;height:640px;background:var(--blue-pale)}
.hero-photo{left:343px;top:139px;width:784px;height:525px;
  background:
    radial-gradient(ellipse 60% 45% at 55% 80%,rgba(255,170,70,.55),transparent 70%),
    linear-gradient(180deg,#7d7fcf 0%,#b996c8 14%,#9a9fc4 22%,#6a7db0 28%,#8a6f8f 40%,#a0604f 58%,#c27a45 74%,#6b3d2e 90%,#3a2420 100%)}
.hero-title{left:75px;top:266px;background:var(--white);padding:0 16px 0 0;font-size:60px;line-height:72px;font-weight:400}
.hero-sub{left:75px;top:352px;background:var(--white);padding:0 14px 4px 0;font-size:35px;color:var(--ink);letter-spacing:.5px}
.hero-since{left:75px;top:416px;font-size:35px;color:var(--ink);letter-spacing:.5px}
.dots{left:75px;top:606px;display:flex;gap:10px}
.dots span{width:25px;height:4px;background:#ddd}
.dots span:first-child{background:var(--blue-mid)}

/* about */
.about-photo1{left:0;top:790px;width:466px;height:415px;
  background:radial-gradient(ellipse 50% 45% at 50% 60%,#c8413e,transparent 75%),linear-gradient(180deg,#9a8c7c 0%,#8a7868 30%,#a8403c 55%,#7c3a34 80%,#8c8478 100%)}
.about-photo2{left:379px;top:965px;width:206px;height:292px;background:linear-gradient(180deg,#c3cbd2 0%,#8e979f 30%,#4a4446 60%,#2a2a2c 100%);border:4px solid var(--white)}
.about-title{left:616px;top:798px;font-size:57px;font-weight:300}
.about-lead{left:616px;top:876px;width:500px;font-style:italic;color:var(--blue-deep);font-size:17px;line-height:30px}
.about-body{left:616px;top:981px;width:506px;font-size:13px;line-height:27px;color:var(--text)}

/* categories */
.cat-title{left:0;top:1362px;width:1200px;text-align:center;font-size:62px}
.card{position:absolute;overflow:hidden}
.card::after{content:"";position:absolute;left:0;right:0;bottom:0;height:45%;background:linear-gradient(180deg,transparent,rgba(0,0,0,.35))}
.card .label{position:absolute;z-index:1;left:18px;bottom:18px;font-family:'Oswald',sans-serif;font-weight:300;font-size:36px;line-height:36px;color:var(--white);text-transform:uppercase}

/* stories */
.story-box{position:absolute;background:var(--white)}
.story-title{font-family:'Oswald',sans-serif;font-weight:400;font-size:24px;line-height:32px;color:var(--blue);text-transform:uppercase}
.story-text{font-size:13px;line-height:27px;color:var(--text);margin-top:14px}

/* footer */
.footer{left:0;top:3991px;width:1200px;height:426px;background:var(--blue-pale)}
.foot-head{font-family:'Oswald',sans-serif;font-weight:400;font-size:21px;color:var(--ink);text-transform:uppercase}
.foot-list{list-style:none;font-family:'Oswald',sans-serif;font-weight:300;font-size:14px;text-transform:uppercase;color:#555}
.site-map li{height:33px}
.quick li{height:38px}
.contact{font-family:'Oswald',sans-serif;font-weight:300;font-size:14px;color:#555;text-transform:uppercase}
.social{display:flex;gap:16px}
.social span{width:18px;height:18px;border-radius:50%;background:#333}
.copyright{left:0;top:4417px;width:1200px;height:64px;border-top:1px solid #e3e3e3;display:flex;align-items:center;justify-content:center;font-size:11px;color:#555}
</style>
</head>
<body>

<header>
  <div class="logo">
    <span class="mark" aria-hidden="true"></span>
    <span class="name">TRAVEL BY MEREL</span>
  </div>
  <nav class="nav">
    <span class="current">Home</span><span>About Me</span><span>Why Book With Us?</span><span>Blog</span><span>Let's Connect</span><span>FAQs</span><span>Forms &amp; Questionnaires</span>
  </nav>
</header>

<section class="hero">
  <div class="abs hero-panel"></div>
  <div class="photo hero-photo" role="img" aria-label="Hillside coastal city at dusk with glowing streets and a bay"></div>
  <h1 class="abs heading hero-title">Travel by Merel</h1>
  <p class="abs hero-sub">Creating Memorable Vacations</p>
  <p class="abs hero-since">Since 1996</p>
  <a class="btn" style="left:75px;top:488px">Read More</a>
  <div class="abs dots"><span></span><span></span><span></span><span></span></div>
</section>

<section class="about">
  <div class="photo about-photo1" role="img" aria-label="Travel agent posing with local children in woven red ponchos on stone steps"></div>
  <div class="photo about-photo2" role="img" aria-label="Portrait of the travel agent at a café"></div>
  <h2 class="abs heading about-title">About Me</h2>
  <p class="abs about-lead">Hello! My name's Merel Hartley, and I'd like to assist you in expertly planning your next vacation—and, hopefully, all those you take in the future.</p>
  <p class="abs about-body">Travel's in my blood! Growing up, my family owned a travel agency and, before I even knew I wanted to be a travel agent, I was off seeing the world—and gaining an appreciation for a well-planned trip.<br>After graduating Northfield Institute of Travel Studies in 1996, I've held management positions with several internationally acclaimed travel companies, gaining a wealth of experience and knowledge that I put to good use when working with clients to design their trips.</p>
  <a class="btn" style="left:616px;top:1196px">Read More</a>
</section>

<section class="categories">
  <h2 class="abs heading cat-title">Categories</h2>
  <div class="card" style="left:75px;top:1478px;width:328px;height:378px;background:radial-gradient(ellipse 45% 40% at 40% 45%,#8b8379,transparent 75%),linear-gradient(180deg,#a8947a 0%,#c9bfae 35%,#b7b0a6 60%,#d9d4cb 100%)" role="img" aria-label="Vintage scooter parked in a stone alley"><span class="label">Custom<br>Travel</span></div>
  <div class="card" style="left:435px;top:1478px;width:330px;height:378px;background:linear-gradient(180deg,#8fb3d0 0%,#b8cfdc 40%,#cfdbe0 58%,#e0d7c4 80%,#cfc3ad 100%)" role="img" aria-label="Family holding hands walking on a beach"><span class="label">Family<br>Vacations</span></div>
  <div class="card" style="left:797px;top:1478px;width:330px;height:378px;background:linear-gradient(100deg,#6e5c4a 0%,#b7ab98 18%,#35a9c0 45%,#4fc0cf 65%,#e8ecea 100%)" role="img" aria-label="Woman under a draped beach cabana by turquoise water"><span class="label">Honeymoon &amp;<br>Romance</span></div>
  <div class="card" style="left:75px;top:1889px;width:513px;height:320px;background:linear-gradient(180deg,#5f7f3e 0%,#476b34 35%,#8f9e8c 52%,#e3e6e8 66%,#27405e 82%,#1d3350 100%)" role="img" aria-label="River cruise ship passing green hills and a castle"><span class="label">River Cruises</span></div>
  <div class="card" style="left:614px;top:1889px;width:513px;height:320px;background:radial-gradient(ellipse 60% 50% at 55% 70%,#e2a98c,transparent 75%),linear-gradient(180deg,#5b9fd6 0%,#9cc4e2 40%,#c9b3a0 70%,#8fb9d4 100%)" role="img" aria-label="Smiling multi-generation family on a sunny beach"><span class="label">Group Travel</span></div>
</section>

<section class="stories">
  <div class="photo" style="left:0;top:2308px;width:704px;height:485px;background:radial-gradient(ellipse 40% 30% at 60% 40%,rgba(240,170,90,.5),transparent 75%),linear-gradient(180deg,#5a4632 0%,#9c6b3a 22%,#a8b6c0 36%,#7c97a8 46%,#6d5a48 62%,#3d2f24 100%)" role="img" aria-label="Diners at a thatched beachside restaurant at sunset"></div>
  <div class="story-box" style="left:640px;top:2379px;width:560px;height:343px;padding:52px 35px 0 35px">
    <h3 class="story-title">The Best Places to Relax and Unwind<br>in the Caribbean</h3>
    <p class="story-text">Something magical happens when Mother Nature puts on a bit of bling. Think of a grown-up, decked-out tree house.<br>Step inside and you connect with nature while, at the same…</p>
  </div>
  <a class="btn" style="left:675px;top:2615px">Read More</a>

  <div class="photo" style="left:496px;top:2868px;width:704px;height:487px;background:linear-gradient(180deg,#1467c0 0%,#3d92d8 30%,#7bc0e6 50%,#47c6cf 60%,#bfe6df 68%,#f2ede2 76%,#f6f2ea 100%)" role="img" aria-label="Palm trees and a white canopy bed on a tropical beach"></div>
  <div class="story-box" style="left:0;top:2939px;width:560px;height:348px;padding:42px 40px 0 75px">
    <h3 class="story-title">6 of the Most Romantic Places<br>in Italy</h3>
    <p class="story-text">Italy is unquestionably a place where art, architecture, history, tradition and nature all combine to create an unforgettable romantic experience. Whether you are travelling with your significant other or travelling to…</p>
  </div>
  <a class="btn" style="left:75px;top:3184px">Read More</a>

  <div class="photo" style="left:0;top:3429px;width:704px;height:487px;background:radial-gradient(ellipse 35% 40% at 62% 62%,#38a9dc,transparent 75%),linear-gradient(100deg,#e4e7ea 0%,#c9d3dc 22%,#3d4d6a 42%,#8a8f98 60%,#c7c9cc 100%)" role="img" aria-label="Expecting couple relaxing in airplane seats"></div>
  <div class="story-box" style="left:640px;top:3499px;width:560px;height:344px;padding:55px 35px 0 35px">
    <h3 class="story-title">Zika Free Babymoons</h3>
    <p class="story-text">Where to Go For Your Perfect Babymoon A Babymoon celebrates that special, fleeting time in a couple's life before a new (and very demanding) addition is welcomed into the family…</p>
  </div>
  <a class="btn" style="left:675px;top:3733px">Read More</a>
</section>

<footer>
  <div class="abs footer"></div>
  <div class="logo" style="top:4043px">
    <span class="mark" aria-hidden="true"></span>
    <span class="name">TRAVEL BY MEREL</span>
  </div>
  <h4 class="abs foot-head" style="left:75px;top:4222px">Contact Us</h4>
  <p class="abs contact" style="left:75px;top:4261px">555-014-2297</p>
  <p class="abs contact" style="left:75px;top:4294px">Email: info@journeywithmerel.example</p>
  <div class="abs social" style="left:75px;top:4347px" aria-label="Social links"><span></span><span></span><span></span><span></span><span></span></div>

  <h4 class="abs foot-head" style="left:358px;top:4038px">Site Map</h4>
  <ul class="abs foot-list site-map" style="left:358px;top:4084px">
    <li>Home</li><li>About Me</li><li>Why Book With Us?</li><li>Blog</li><li>Let's Connect</li><li>FAQs</li><li>Forms &amp; Questionnaires</li>
  </ul>

  <h4 class="abs foot-head" style="left:600px;top:4038px">Quick Links</h4>
  <ul class="abs foot-list quick" style="left:600px;top:4084px">
    <li>Posts About Custom Trips</li><li>Posts About Honeymoons &amp; Romance</li><li>Posts About Family Travel</li><li>Posts About Cruise Vacations</li><li>Posts About Travel Tips</li><li>Welcome Home</li><li>Booking Fee</li><li>Plan To Go Service Agreement</li>
  </ul>
  <ul class="abs foot-list quick" style="left:899px;top:4084px">
    <li>Plan To Go Service Agreement</li><li>Cancellation Fee</li><li>Airline Ticket Fee</li><li>Concierge Services</li><li>Payment Form</li><li>Transfer Your Cruise Booking</li><li>Archives</li><li>Press Releases</li>
  </ul>

  <div class="abs copyright">Copyright © 2024 Company Name. All Rights Reserved</div>
</footer>

</body>
</html>
```